Mobile friendly Website design

Client is a packaging equipment company that would like a clean, mobile friendly design. They want a different home page than what they have now. The home page should have the traditional sliders, content area, services are and a featured products area. Please provide an internal page design too.

Target Market(s)

Companies who use packaging equipment, shrink wrappers, heat sealers and carton erectors.

Industry/Entity Type

It Company

Number of Pages Required

2 page

Font styles to use
Serif
Sans Serif

Requirements
Must have
• Must have a clean, mobile friendly design.

```html
<!DOCTYPE html>
<html lang="en">
<head>
<meta charset="utf-8">
<title>Halbrook Companies</title>
<link href="https://fonts.googleapis.com/css2?family=Open+Sans:ital,wght@0,400;0,600;0,700;1,400&display=swap" rel="stylesheet">
<style>
:root{
  --red:#9b1b30;
  --navy:#1d2050;
  --text:#555;
  --light:#ececec;
  --footer:#4a4a4a;
  --footer-dark:#2b2b2b;
  --white:#fff;
}
*{margin:0;padding:0;box-sizing:border-box}
html,body{width:1200px;height:3169px;overflow:hidden}
body{font-family:"Open Sans",sans-serif;color:var(--text);background:var(--white);position:relative}
.abs{position:absolute}

/* header */
.welcome{left:173px;top:32px;font-size:14px;color:#888}
.welcome b{color:var(--navy);font-weight:400}
.brand{left:0;width:1200px;top:20px;text-align:center;font-size:38px;font-weight:700;color:var(--red);line-height:50px}
.phone{left:888px;top:27px;display:flex;align-items:center;gap:14px;font-size:15px;color:#666}
.nav{left:0;top:89px;width:1200px;height:50px;background:var(--light)}
.nav a{position:absolute;top:15px;font-size:14px;color:#333;text-decoration:none}
.nav a.active{color:var(--red)}
.search{left:1000px;top:9px;width:30px;height:30px;border:1.5px solid var(--navy)}

/* hero */
.hero{left:0;top:139px;width:1200px;height:503px;background:linear-gradient(120deg,#6b6660 0%,#8a8178 40%,#b4aa9c 70%,#d2c9bd 100%)}
.hero-shade{inset:0;background:rgba(20,20,20,.35)}
.hero h1{left:0;width:1200px;top:178px;text-align:center;color:var(--white);font-size:30px;font-weight:600;letter-spacing:1px}
.hero p{left:0;width:1200px;top:231px;text-align:center;color:var(--white);font-size:23px}
.btn-more{left:545px;top:334px;width:110px;height:46px;border:1.5px solid var(--white);border-radius:23px;color:var(--white);font-size:12px;text-align:center;line-height:43px}
.arrow{width:40px;height:40px;border:1.5px solid var(--white);border-radius:50%}

/* section headings */
.sec-title{left:0;width:1200px;text-align:center;font-size:28px;font-weight:600}
.rule{left:575px;width:50px;height:3px}

/* services */
.lead{left:211px;width:778px;top:784px;text-align:center;font-size:15px;line-height:28px}
.svc{width:203px;top:904px}
.svc-frame{width:203px;height:203px;border:1px solid #ddd;padding:8px}
.svc-img{width:100%;height:100%}
.svc h3{margin-top:22px;font-size:15px;font-weight:700;color:var(--red);padding-left:8px}
.svc p{margin-top:6px;font-size:12px;line-height:19px;color:#777;padding-left:8px}
.dot{top:1251px;width:11px;height:11px;border-radius:50%;background:#bbb}

/* what we do */
.worker{left:0;top:1300px;width:575px;height:460px;background:linear-gradient(160deg,#d62a2a,#b81f24 45%,#c7a27a 80%,#fff 100%)}
.wwd-title{left:583px;top:1355px;font-size:38px;font-weight:600;color:var(--navy)}
.wwd-item{left:583px;width:440px;display:flex;gap:20px}
.wwd-icon{flex:none;width:36px;height:36px;border:1px solid #ccc;border-radius:4px;display:flex;align-items:center;justify-content:center;box-shadow:0 1px 3px rgba(0,0,0,.15)}
.wwd-item p{font-size:13px;line-height:22px;color:#666}

/* products */
.products{left:0;top:1760px;width:1200px;height:454px;background:var(--light)}
.prod{top:1931px;width:275px;height:283px;background:var(--white);padding:8px}
.prod-img{width:259px;height:215px}
.prod h3{margin-top:20px;text-align:center;font-size:19px;font-weight:600;color:var(--navy)}
.arrow-dark{width:40px;height:40px;border:1.5px solid #999;border-radius:50%;background:var(--white)}

/* testimonials */
.testi-title{left:173px;top:2288px;font-size:29px;color:var(--red)}
.testi{top:2398px;width:368px}
.testi-img{width:368px;height:201px}
.testi h3{margin-top:24px;font-size:15px;font-weight:700;color:var(--navy);padding-left:10px}
.testi blockquote{margin-top:10px;padding-left:20px;font-size:13px;line-height:22px;font-style:italic;color:#777;position:relative}
.testi blockquote::before{content:"\201C";position:absolute;left:0;top:-6px;font-size:34px;color:#bbb;font-style:normal}

/* footer */
.footer{left:0;top:2772px;width:1200px;height:319px;background:var(--footer);color:#ddd}
.fcol{top:70px}
.fcol h4{font-size:16px;font-weight:400;color:var(--white);margin-bottom:24px}
.fcol li{list-style:none;font-size:13px;line-height:32px}
.fcol .note{font-size:12px;line-height:19px;width:200px}
.field{margin-top:20px;width:190px;height:30px;border:1px solid #999;display:flex;align-items:center;padding-left:8px}
.submit{margin-top:12px;width:60px;height:24px;background:#999;color:var(--white);font-size:10px;text-align:center;line-height:24px}
.social{width:28px;height:28px;border-radius:50%;background:var(--white);margin-bottom:16px}
.contact li{display:flex;gap:14px;line-height:20px;margin-bottom:20px}
.contact li::before{content:"";flex:none;width:8px;height:8px;border-radius:50%;background:#ccc;margin-top:6px}
.copy{left:0;top:3091px;width:1200px;height:78px;background:var(--footer-dark);color:#aaa;font-size:13px;text-align:center;line-height:78px}
</style>
</head>
<body>

<header>
  <div class="abs welcome">Welcome to <b>Halbrook Companies</b></div>
  <div class="abs brand">Halbrook</div>
  <div class="abs phone">
    <svg width="28" height="28" viewBox="0 0 28 28"><circle cx="14" cy="14" r="13" fill="none" stroke="#9b1b30" stroke-width="1.5"/><path d="M10 8l3 3-1.5 2a8 8 0 0 0 3.5 3.5l2-1.5 3 3-2 2c-5 0-10-5-10-10z" fill="#9b1b30"/></svg>
    (555) 014-2290
  </div>
  <nav class="abs nav">
    <a class="active" style="left:190px">Home</a>
    <a style="left:287px">About Us</a>
    <a style="left:404px">Packaging</a>
    <a style="left:528px">Products</a>
    <a style="left:644px">Support</a>
    <a style="left:754px">Contact</a>
    <div class="abs search"><svg width="27" height="27" viewBox="0 0 27 27"><circle cx="12" cy="12" r="6" fill="none" stroke="#1d2050" stroke-width="2"/><path d="M16.5 16.5l5 5" stroke="#1d2050" stroke-width="2"/></svg></div>
  </nav>
</header>

<section class="abs hero" role="img" aria-label="Smiling couple carrying cardboard boxes in a home by a staircase">
  <div class="abs hero-shade"></div>
  <h1 class="abs">PROIN TINCIDUNT FERMENTUM PLACERAT</h1>
  <p class="abs">Sit amet ornare magna faucibus cras imperdiet lacus ut urna cursus maximus</p>
  <div class="abs btn-more">KNOE MORE</div>
  <div class="abs arrow" style="left:100px;top:205px"><svg width="37" height="37"><path d="M21 12l-6 6.5 6 6.5" fill="none" stroke="#fff" stroke-width="2"/></svg></div>
  <div class="abs arrow" style="left:1062px;top:205px"><svg width="37" height="37"><path d="M16 12l6 6.5-6 6.5" fill="none" stroke="#fff" stroke-width="2"/></svg></div>
</section>

<section>
  <h2 class="abs sec-title" style="top:724px;color:var(--red)">SERVICES</h2>
  <div class="abs rule" style="top:770px;background:var(--red)"></div>
  <p class="abs lead">Morbi auctor tincidunt libero eget facilisis. Fusce venenatis purus in risus maximus mauris efficitur leo vitae aliquet porttitor. Sed eu turpis eu dui luctus dignissim eget ut libero.</p>

  <article class="abs svc" style="left:173px">
    <div class="svc-frame"><div class="svc-img" role="img" aria-label="Family with moving boxes" style="background:linear-gradient(#eeeae4,#c9a77e)"></div></div>
    <h3>INTEGER VARIUS</h3>
    <p>Mauris lacinia eros ac felis vulputate, sit amet ornare magna faucibus. Cras imperdiet lacus ut urna cursus maximus.</p>
  </article>
  <article class="abs svc" style="left:391px">
    <div class="svc-frame"><div class="svc-img" role="img" aria-label="Courier in red uniform holding a parcel" style="background:linear-gradient(#e9e9e9,#c8342f 60%,#b98d5d)"></div></div>
    <h3>INTEGER VARIUS</h3>
    <p>Mauris lacinia eros ac felis vulputate, sit amet ornare magna faucibus. Cras imperdiet lacus ut urna cursus maximus.</p>
  </article>
  <article class="abs svc" style="left:611px">
    <div class="svc-frame"><div class="svc-img" role="img" aria-label="Movers loading boxes into a van" style="background:linear-gradient(#d9dde2,#8a96a4 60%,#a88660)"></div></div>
    <h3>INTEGER VARIUS</h3>
    <p>Mauris lacinia eros ac felis vulputate, sit amet ornare magna faucibus. Cras imperdiet lacus ut urna cursus maximus.</p>
  </article>
  <article class="abs svc" style="left:828px">
    <div class="svc-frame"><div class="svc-img" role="img" aria-label="Delivery driver with clipboard beside a van" style="background:linear-gradient(#dfe6ee,#5a78a8 60%,#b89470)"></div></div>
    <h3>INTEGER VARIUS</h3>
    <p>Mauris lacinia eros ac felis vulputate, sit amet ornare magna faucibus. Cras imperdiet lacus ut urna cursus maximus.</p>
  </article>
  <div class="abs dot" style="left:577px;background:var(--red)"></div>
  <div class="abs dot" style="left:594px"></div>
  <div class="abs dot" style="left:611px"></div>
</section>

<section>
  <div class="abs worker" role="img" aria-label="Delivery man in red cap and jacket holding a cardboard box"></div>
  <h2 class="abs wwd-title">What We Do</h2>
  <div class="abs wwd-item" style="top:1450px">
    <div class="wwd-icon"><svg width="22" height="22"><rect x="3" y="5" width="16" height="12" fill="none" stroke="#9b1b30" stroke-width="2"/><path d="M3 9h16" stroke="#9b1b30" stroke-width="2"/></svg></div>
    <p>Mauris efficitur leo vitae aliquet porttitor. Sed eu turpis eu dui luctus dignissim eget ut libero. Phasellus malesuada sapien erat, eu placerat est scelerisque suscipit.</p>
  </div>
  <div class="abs wwd-item" style="top:1545px">
    <div class="wwd-icon"><svg width="22" height="22"><rect x="2" y="7" width="12" height="8" fill="#9b1b30"/><path d="M14 9h4l2 3v3h-6z" fill="#9b1b30"/><circle cx="6" cy="17" r="2" fill="#9b1b30"/><circle cx="16" cy="17" r="2" fill="#9b1b30"/></svg></div>
    <p>Mauris efficitur leo vitae aliquet porttitor. Sed eu turpis eu dui luctus dignissim eget ut libero. Phasellus malesuada sapien erat, eu placerat est scelerisque suscipit.</p>
  </div>
  <div class="abs wwd-item" style="top:1640px">
    <div class="wwd-icon"><svg width="22" height="22"><rect x="6" y="3" width="10" height="16" fill="none" stroke="#9b1b30" stroke-width="2"/><path d="M9 8h4M9 12h4" stroke="#9b1b30" stroke-width="2"/></svg></div>
    <p>Mauris efficitur leo vitae aliquet porttitor. Sed eu turpis eu dui luctus dignissim eget ut libero. Phasellus malesuada sapien erat, eu placerat est scelerisque suscipit.</p>
  </div>
</section>

<section>
  <div class="abs products"></div>
  <h2 class="abs sec-title" style="top:1845px;color:var(--navy);font-size:27px">OUR FEATURED PRODUCTS</h2>
  <div class="abs rule" style="top:1891px;width:40px;left:580px;background:var(--navy)"></div>
  <div class="abs arrow-dark" style="left:100px;top:2046px"><svg width="37" height="37"><path d="M21 12l-6 6.5 6 6.5" fill="none" stroke="#777" stroke-width="2"/></svg></div>
  <div class="abs arrow-dark" style="left:1062px;top:2046px"><svg width="37" height="37"><path d="M16 12l6 6.5-6 6.5" fill="none" stroke="#777" stroke-width="2"/></svg></div>
  <article class="abs prod" style="left:173px">
    <div class="prod-img" role="img" aria-label="Red tape dispenser on a carton" style="background:linear-gradient(#eee2cf,#c7a273 55%,#c8383a)"></div>
    <h3>PACKAGING EQUIPMENT</h3>
  </article>
  <article class="abs prod" style="left:465px">
    <div class="prod-img" role="img" aria-label="Rolls of clear shrink wrap film" style="background:linear-gradient(#f4f4f4,#b9bcc0 50%,#e3e4e6)"></div>
    <h3>SHRINK WRAPPERS</h3>
  </article>
  <article class="abs prod" style="left:756px">
    <div class="prod-img" role="img" aria-label="Carton sealing machine" style="background:linear-gradient(#cfb28a,#a9a9a9 55%,#dcdcdc)"></div>
    <h3>PACKAGING EQUIPMENT</h3>
  </article>
</section>

<section>
  <h2 class="abs testi-title">What Client Says About Us</h2>
  <article class="abs testi" style="left:173px">
    <div class="testi-img" role="img" aria-label="Portrait of a smiling client in a denim shirt" style="background:linear-gradient(90deg,#cbbfae,#7d8fa6 55%,#c9b9a3)"></div>
    <h3>INTEGER VARIUS TEMPOR</h3>
    <blockquote>Cras mattis dolor vitae risus maximus, sit amet iaculis dui hendrerit. Proin sagittis elementum eros. Suspendisse vel porta velit. Morbi ac pretium lectus</blockquote>
  </article>
  <article class="abs testi" style="left:661px">
    <div class="testi-img" role="img" aria-label="Portrait of a smiling client with long dark hair" style="background:linear-gradient(90deg,#2a2420,#6a4a3a 50%,#2a8a9a)"></div>
    <h3>INTEGER VARIUS TEMPOR</h3>
    <blockquote>Cras mattis dolor vitae risus maximus, sit amet iaculis dui hendrerit. Proin sagittis elementum eros. Suspendisse vel porta velit. Morbi ac pretium lectus</blockquote>
  </article>
</section>

<footer class="abs footer">
  <div class="abs fcol" style="left:182px">
    <h4>MENU</h4>
    <ul><li>Home</li><li>About Us</li><li>Packaging</li><li>Products</li><li>Support</li><li>Contact</li></ul>
  </div>
  <div class="abs fcol" style="left:397px">
    <h4>NEWSLETTER</h4>
    <p class="note">Keep up with the latest company news and events. Enter your e-mail and subscribe to our newsletter</p>
    <div class="field"><svg width="16" height="12"><rect x="1" y="1" width="14" height="10" fill="none" stroke="#bbb"/><path d="M1 1l7 5 7-5" fill="none" stroke="#bbb"/></svg></div>
    <div class="submit">SUBMIT</div>
  </div>
  <div class="abs fcol" style="left:617px">
    <h4>FOLLOW US</h4>
    <div class="social"></div><div class="social"></div><div class="social"></div><div class="social"></div>
  </div>
  <div class="abs fcol contact" style="left:830px">
    <h4>GET IN TOUCH</h4>
    <ul style="font-size:13px"><li>120 Linden Avenue<br>Portvale, PV4 2RS.</li><li>hello@halbrook.example</li><li>555-014-331</li></ul>
  </div>
</footer>
<div class="abs copy">© 2016 halbrook all reserved</div>

</body>
</html>
```